Facebook Cover Photo for Cosmetic Injection and Spray Tanning Salon

We are looking for a new FB Cover Photo for our Cosmetic Injection and Air Brush Spray tanning Salon. The company is Bright Fern Salon (www.brightfernsalon.example) we currently have one but we need something new and fresh designed with the proper size requirements for desktop/mobile. Professional looking

Target Market(s)

80% Female Market ages between 14-65
Remaining Males

Industry/Entity Type

Beauty

Requirements
Must have
• Services:
• Cosmetic Injections
• Air Brush Spray Tanning
• Lash Growth Serum & Skin Care Products
• Address: 438 Tamsin street. Port Perry, ON. K4R 2C9
• Phone: 905 461 7380
• Website: www.brightfernsalon.example
• Email: dana@brightfernsalon.example
Nice to have
• We want to see some designs using a black background as well.

```html
<!DOCTYPE html>
<html lang="en">
<head>
<meta charset="utf-8">
<title>Bright Fern Salon – Facebook Covers</title>
<link rel="stylesheet" href="https://fonts.googleapis.com/css2?family=Open+Sans:wght@400&family=Raleway:wght@300;400;500;800&display=swap">
<style>
  :root {
    --stage: #474747;
    --label: #f2f2f2;
    --ink: #0a0a0c;
    --pink: #ec1a77;
    --violet: #7a7fc4;
    --white: #ffffff;
  }
  html, body {
    margin: 0;
    width: 1200px;
    height: 1200px;
    overflow: hidden;
    background: radial-gradient(circle at 50% 50%, #525252 0%, var(--stage) 70%);
    font-family: "Raleway", sans-serif;
  }
  .board {
    position: relative;
    width: 1200px;
    height: 1200px;
  }
  .cover-block {
    position: absolute;
    left: 50px;
    width: 1100px;
  }
  .cover-block--first { top: 118px; }
  .cover-block--second { top: 652px; }
  .cover-label {
    margin: 0 0 16px;
    font-family: "Open Sans", sans-serif;
    font-size: 19px;
    font-weight: 400;
    color: var(--label);
  }
  .cover {
    display: block;
    width: 1100px;
    height: 416px;
    box-shadow: 0 6px 18px rgba(0,0,0,0.35);
  }
  .headline-bold { font-weight: 800; fill: var(--white); }
  .headline-light { font-weight: 300; fill: var(--white); }
  .services-title { font-weight: 400; fill: var(--white); font-size: 17px; }
  .service-item { font-weight: 500; fill: var(--white); font-size: 17px; }
  .contact-line { font-weight: 400; fill: var(--white); font-size: 15px; }
</style>
</head>
<body>
<main class="board">

  <section class="cover-block cover-block--first">
    <h2 class="cover-label">Bright Fern Salon Facebook Cover-1</h2>
    <svg class="cover" viewBox="0 0 828 313" xmlns="http://www.w3.org/2000/svg" font-family="Raleway, sans-serif">
      <defs>
        <radialGradient id="night-sky" cx="60%" cy="40%" r="80%">
          <stop offset="0" stop-color="#1a1a22"/>
          <stop offset="1" stop-color="#050507"/>
        </radialGradient>
        <radialGradient id="skin-tone-a" cx="50%" cy="45%" r="60%">
          <stop offset="0" stop-color="#f3dccd"/>
          <stop offset="1" stop-color="#c9a18c"/>
        </radialGradient>
        <radialGradient id="skin-tone-b" cx="50%" cy="45%" r="60%">
          <stop offset="0" stop-color="#f7e3d6"/>
          <stop offset="1" stop-color="#d9b29c"/>
        </radialGradient>
      </defs>

      <rect class="cover-bg" width="828" height="313" fill="url(#night-sky)"/>

      <!-- headline band -->
      <rect class="headline-band" x="0" y="36" width="450" height="56" fill="var(--pink)"/>
      <text x="10" y="80" font-size="40"><tspan class="headline-bold">BRIGHT FERN </tspan><tspan class="headline-light">SALON</tspan></text>

      <!-- services -->
      <g class="services">
        <line x1="12" y1="112" x2="28" y2="112" stroke="var(--pink)" stroke-width="3"/>
        <text class="services-title" x="31" y="118">SERVICES</text>
        <line x1="115" y1="112" x2="131" y2="112" stroke="var(--pink)" stroke-width="3"/>
        <circle cx="15" cy="140" r="3.5" fill="var(--pink)"/>
        <text class="service-item" x="24" y="146">Cosmetic Injections</text>
        <circle cx="193" cy="140" r="3.5" fill="var(--pink)"/>
        <text class="service-item" x="201" y="146">Air Brush Spray Tanning</text>
        <circle cx="15" cy="165" r="3.5" fill="var(--pink)"/>
        <text class="service-item" x="25" y="171">Lash Growth Serum &amp; Skin Care Products</text>
      </g>

      <!-- contact strip -->
      <g class="contact">
        <rect x="0" y="200" width="24" height="113" fill="var(--violet)"/>
        <path d="M8 208 q-3 6 0 12 M16 210 q2 4 0 8" stroke="var(--white)" stroke-width="2" fill="none"/>
        <rect x="5" y="235" width="14" height="10" fill="var(--white)"/>
        <path d="M5 235 l7 6 l7 -6" stroke="var(--violet)" stroke-width="1.5" fill="none"/>
        <circle cx="12" cy="264" r="7" stroke="var(--white)" stroke-width="1.5" fill="none"/>
        <path d="M5 264 h14 M12 257 v14" stroke="var(--white)" stroke-width="1"/>
        <path d="M12 297 c-6 -7 -6 -11 0 -12 c6 1 6 5 0 12z" fill="var(--white)"/>
        <text class="contact-line" x="36" y="220">905 461 7380</text>
        <text class="contact-line" x="36" y="245">dana@brightfernsalon.example</text>
        <text class="contact-line" x="36" y="268">www.brightfernsalon.example</text>
        <text class="contact-line" x="36" y="294">438 Tamsin street. Port Perry, ON. K4R 2C9</text>
      </g>

      <!-- right decor -->
      <rect x="753" y="188" width="75" height="56" fill="var(--violet)"/>
      <rect x="461" y="305" width="367" height="8" fill="var(--pink)"/>

      <circle cx="525" cy="114" r="96" fill="none" stroke="var(--pink)" stroke-width="30"/>
      <g role="img" aria-label="Close-up photo of a woman receiving a cosmetic injection">
        <circle cx="525" cy="114" r="80" fill="url(#skin-tone-a)"/>
      </g>

      <circle cx="698" cy="192" r="76" fill="none" stroke="var(--violet)" stroke-width="14"/>
      <circle cx="698" cy="192" r="66" fill="var(--white)"/>
      <g role="img" aria-label="Photo of a woman checking her smooth forehead skin">
        <circle cx="698" cy="192" r="60" fill="url(#skin-tone-b)"/>
      </g>
    </svg>
  </section>

  <section class="cover-block cover-block--second">
    <h2 class="cover-label">Bright Fern Salon Facebook Cover-2</h2>
    <svg class="cover" viewBox="0 0 828 313" xmlns="http://www.w3.org/2000/svg" font-family="Raleway, sans-serif">
      <defs>
        <linearGradient id="dark-curtain" x1="0" y1="0" x2="1" y2="0">
          <stop offset="0" stop-color="#0c0c0e"/>
          <stop offset="0.5" stop-color="#18181b"/>
          <stop offset="1" stop-color="#0a0a0c"/>
        </linearGradient>
        <radialGradient id="skin-tone-c" cx="50%" cy="45%" r="60%">
          <stop offset="0" stop-color="#f3dccd"/>
          <stop offset="1" stop-color="#c9a18c"/>
        </radialGradient>
        <radialGradient id="tan-tone" cx="40%" cy="50%" r="70%">
          <stop offset="0" stop-color="#e2a67e"/>
          <stop offset="1" stop-color="#a8694a"/>
        </radialGradient>
      </defs>

      <rect class="cover-bg" width="828" height="313" fill="url(#dark-curtain)"/>

      <rect class="headline-band" x="0" y="36" width="450" height="56" fill="var(--pink)"/>
      <text x="10" y="80" font-size="40"><tspan class="headline-bold">BRIGHT FERN </tspan><tspan class="headline-light">SALON</tspan></text>

      <g class="services">
        <line x1="12" y1="112" x2="28" y2="112" stroke="var(--pink)" stroke-width="3"/>
        <text class="services-title" x="31" y="118">SERVICES</text>
        <line x1="115" y1="112" x2="131" y2="112" stroke="var(--pink)" stroke-width="3"/>
        <circle cx="15" cy="140" r="3.5" fill="var(--pink)"/>
        <text class="service-item" x="24" y="146">Cosmetic Injections</text>
        <circle cx="193" cy="140" r="3.5" fill="var(--pink)"/>
        <text class="service-item" x="201" y="146">Airbrush Spray Tanning</text>
        <circle cx="15" cy="165" r="3.5" fill="var(--pink)"/>
        <text class="service-item" x="25" y="171">Lash Growth Serum &amp; Skin Care Products</text>
      </g>

      <g class="contact">
        <rect x="0" y="200" width="24" height="113" fill="var(--violet)"/>
        <path d="M8 208 q-3 6 0 12 M16 210 q2 4 0 8" stroke="var(--white)" stroke-width="2" fill="none"/>
        <rect x="5" y="235" width="14" height="10" fill="var(--white)"/>
        <path d="M5 235 l7 6 l7 -6" stroke="var(--violet)" stroke-width="1.5" fill="none"/>
        <circle cx="12" cy="264" r="7" stroke="var(--white)" stroke-width="1.5" fill="none"/>
        <path d="M5 264 h14 M12 257 v14" stroke="var(--white)" stroke-width="1"/>
        <path d="M12 297 c-6 -7 -6 -11 0 -12 c6 1 6 5 0 12z" fill="var(--white)"/>
        <text class="contact-line" x="36" y="220">905 461 7380</text>
        <text class="contact-line" x="36" y="245">dana@brightfernsalon.example</text>
        <text class="contact-line" x="36" y="268">www.brightfernsalon.example</text>
        <text class="contact-line" x="36" y="294">438 Tamsin street. Port Perry, ON. K4R 2C9</text>
      </g>

      <rect x="753" y="188" width="75" height="56" fill="var(--violet)"/>
      <rect x="461" y="305" width="367" height="8" fill="var(--pink)"/>

      <circle cx="525" cy="114" r="96" fill="none" stroke="var(--pink)" stroke-width="30"/>
      <g role="img" aria-label="Close-up photo of a woman receiving a cosmetic injection">
        <circle cx="525" cy="114" r="80" fill="url(#skin-tone-c)"/>
      </g>

      <circle cx="698" cy="192" r="76" fill="none" stroke="var(--violet)" stroke-width="14"/>
      <circle cx="698" cy="192" r="66" fill="var(--white)"/>
      <g role="img" aria-label="Photo of an airbrush spray tan being applied to a body">
        <circle cx="698" cy="192" r="60" fill="url(#tan-tone)"/>
      </g>
    </svg>
  </section>

</main>
</body>
</html>
```